Recruitment talent email to send employers

We are a recruitment company specialising in STEM talent. We're after an eye catching email design to send our clients (ie employers) information about our top cadidates.

Target Market(s)

Employers

Requirements
Must have
• Must be clean/fresh looking, professional and concise

```html
<!DOCTYPE html>
<html lang="en">
<head>
<meta charset="utf-8">
<title>Top Talents For Your Company</title>
<link href="https://fonts.googleapis.com/css2?family=Lato:wght@300;400;700;900&display=swap" rel="stylesheet">
<style>
  :root {
    --page-bg: #ffffff;
    --hero-dark: #2b2b2b;
    --hero-mid: #5a5650;
    --hero-light: #8a8580;
    --card-bg: #ededed;
    --text-main: #222222;
    --text-muted: #7a7a7a;
    --accent: #f5494a;
    --link: #3a8fd8;
    --rule: #cfcfcf;
    --white: #ffffff;
  }
  * { margin: 0; padding: 0; box-sizing: border-box; }
  html, body { width: 863px; height: 1200px; overflow: hidden; background: var(--page-bg); }
  body { font-family: "Lato", Arial, sans-serif; color: var(--text-main); position: relative; }

  .hero {
    position: absolute; left: 89px; top: 0; width: 681px; height: 236px;
    background: linear-gradient(100deg, var(--hero-mid) 0%, var(--hero-dark) 45%, var(--hero-light) 100%);
    overflow: hidden;
  }
  .hero-photo { position: absolute; inset: 0; background: radial-gradient(ellipse at 60% 55%, rgba(170,140,120,0.35), transparent 60%); }
  .brand {
    position: absolute; left: 52px; top: 34px; display: flex; align-items: center; gap: 9px;
    color: var(--white); font-weight: 700; font-size: 17px; letter-spacing: 0.5px;
  }
  .brand-mark { width: 12px; height: 12px; background: var(--white); border-radius: 50%; }
  .hero-title {
    position: absolute; left: 48px; top: 130px; color: var(--white);
    font-weight: 700; font-size: 38px; line-height: 47px; letter-spacing: 1.6px;
  }

  .greeting { position: absolute; left: 110px; top: 266px; font-size: 12.5px; line-height: 17px; }

  .candidate {
    position: absolute; left: 96px; width: 663px; height: 352px; background: var(--card-bg);
  }
  .candidate--first { top: 346px; }
  .candidate--second { top: 717px; }
  .avatar {
    position: absolute; left: 56px; top: 14px; width: 76px; height: 76px; border-radius: 50%;
    border: 3px solid var(--white);
    background: radial-gradient(circle at 50% 40%, #b08a78, #5b3a30 70%, #2a2624);
  }
  .name { position: absolute; left: 156px; top: 30px; font-size: 17px; }
  .role { position: absolute; left: 156px; top: 55px; font-size: 14.5px; font-weight: 300; color: var(--text-muted); }
  .label { position: absolute; width: 134px; text-align: right; font-size: 12.5px; color: var(--text-muted); font-weight: 300; }
  .value { position: absolute; left: 156px; font-size: 12.5px; line-height: 17px; }
  .view-profile {
    position: absolute; left: 153px; top: 293px; width: 102px; height: 25px; border-radius: 6px;
    background: var(--accent); color: var(--white); font-size: 12.5px; line-height: 25px; text-align: center;
  }

  .help { position: absolute; left: 106px; top: 1080px; font-size: 12.5px; line-height: 17px; }
  .help a { color: var(--link); text-decoration: none; }
  .footer-rule { position: absolute; left: 101px; top: 1129px; width: 658px; height: 2px; background: var(--rule); }
  .copyright { position: absolute; left: 101px; top: 1167px; font-size: 12.5px; }
</style>
</head>
<body>
  <header class="hero">
    <div class="hero-photo" role="img" aria-label="Photo of two people shaking hands in an office"></div>
    <div class="brand"><span class="brand-mark"></span>Northbeam Talent</div>
    <h1 class="hero-title">Top Talents<br>For Your Company</h1>
  </header>

  <p class="greeting">Hi,<br>We have got some of the top talents for<br>&lt;The Position Name&gt;</p>

  <section class="candidate candidate--first">
    <div class="avatar" role="img" aria-label="Candidate portrait photo"></div>
    <div class="name">Marcus Feld</div>
    <div class="role">Software Engineer</div>
    <div class="label" style="top:103px">Experince:</div>
    <div class="value" style="top:102px">7 years</div>
    <div class="label" style="top:126px">Work:</div>
    <div class="value" style="top:125px">Software Engineer . Brightlane&nbsp; Jan ‘15 - Feb ‘18</div>
    <div class="value" style="top:147px">Software Engineer . Corvell Partners&nbsp;&nbsp; Oct ‘14 - Jan ‘15</div>
    <div class="label" style="top:182px">School:</div>
    <div class="value" style="top:181px">Eastbrook University2013<br>BA German Studies</div>
    <div class="value" style="top:226px">Eastbrook University2013<br>BSE Computer Science and Engineering</div>
    <div class="view-profile">View Profile</div>
  </section>

  <section class="candidate candidate--second">
    <div class="avatar" role="img" aria-label="Candidate portrait photo"></div>
    <div class="name">Marcus Feld</div>
    <div class="role">Software Engineer</div>
    <div class="label" style="top:103px">Experince:</div>
    <div class="value" style="top:102px">7 years</div>
    <div class="label" style="top:126px">Work:</div>
    <div class="value" style="top:125px">Software Engineer . Brightlane&nbsp;&nbsp; Jan ‘15 - Feb ‘18</div>
    <div class="value" style="top:147px">Software Engineer . Corvell Partners&nbsp;&nbsp;&nbsp; Oct ‘14 - Jan ‘15</div>
    <div class="label" style="top:182px">School:</div>
    <div class="value" style="top:181px">Eastbrook University2013<br>BA German Studies</div>
    <div class="value" style="top:226px">Eastbrook University2013<br>BSE Computer Science and Engineering</div>
    <div class="view-profile">View Profile</div>
  </section>

  <p class="help">Need help?<br>Contact <a href="#">Customer Support</a> for assistance</p>
  <div class="footer-rule"></div>
  <p class="copyright">© 2019 - The Northbeam Talent Group.</p>
</body>
</html>
```